Business Card and Letterhead for Law Firm
Tolland & Reeve, P.C. Attorneys and Counselors at Law
Business Card and Letterhead for Law Firm - Law
Simple
Corwin T. Tolland, Esq.
Partner
83 E. Birchfield Ln Hicksville, NY 11947 T. 516-555-0142 F. 516-555-0187 314 Halvorsen Avenue, Suite 2200 New York, NY 10038 T. 212-555-0163 F.
ctolland@tollandlegal.example
www.tollandlegal.example
Need same business card for Gerald Bertram Reeve, Esq. Partner (SAME ADDRESSES) email: greeve@tollandlegal.example
TollandReeveLaw TollandReeveLaw
Please check the uploaded logo for the stationary and business cards.
For letterhead- Addresses should be at the FOOTER and the HEADER should have logo in center; Names of attorneys CORWIN T. TOLLAND, ESQ. (Admitted in NY and NJ) and GERALD BERTRAM REEVE, ESQ. (Admiited in NY).

```html
<!DOCTYPE html>
<html lang="en">
<head>
<meta charset="utf-8">
<title>Tolland &amp; Reeve, P.C. — Stationery Concepts</title>
<link href="https://fonts.googleapis.com/css2?family=Crimson+Text:wght@400;600&family=Open+Sans:wght@400;600&family=Great+Vibes&display=swap" rel="stylesheet">
<style>
:root{
  --bg:#1b1b1b;
  --navy:#1d4a6e;
  --navy-dark:#153750;
  --paper:#ffffff;
  --paper-soft:#eeeeee;
  --grey:#6e6e6e;
  --ink:#333333;
  --line:#c9c9c9;
  --white:#ffffff;
}
*{margin:0;padding:0;box-sizing:border-box}
html,body{width:1200px;height:254px;overflow:hidden;background:var(--bg)}
body{position:relative;font-family:"Open Sans",Arial,sans-serif;color:var(--ink)}
.piece{position:absolute;background:var(--paper);overflow:hidden}
.navy{background:var(--navy);color:var(--white)}
.grey{background:var(--grey);color:var(--white)}
.caption{position:absolute;font-family:"Crimson Text",serif;font-size:2.4px;color:#9a9a9a;text-align:center;white-space:nowrap}

/* firm name lockup */
.firm{position:absolute;display:flex;align-items:center;gap:.35em;font-family:"Crimson Text",serif;color:var(--navy);white-space:nowrap;line-height:1}
.firm .mark{width:.9em;height:.9em;background:currentColor;flex:none}
.firm .name{font-size:1em;font-weight:600;letter-spacing:.02em}
.firm .tag{display:block;font-size:.42em;letter-spacing:.06em;text-transform:uppercase;font-weight:400;margin-top:.15em}
.on-dark .firm,.firm.light{color:var(--white)}

.body-lines{position:absolute;display:flex;flex-direction:column;gap:1.6px}
.body-lines i{display:block;height:.6px;background:var(--line)}
.tiny{position:absolute;font-size:2px;line-height:1.35;color:var(--ink);white-space:nowrap}
.web{position:absolute;font-size:2.1px;letter-spacing:.08em;white-space:nowrap}
.script{position:absolute;font-family:"Great Vibes",cursive;color:var(--navy);white-space:nowrap}

.heading{position:absolute;font-family:"Open Sans",Arial,sans-serif;font-weight:600;color:var(--navy);font-size:4.2px;line-height:1}
.sub{position:absolute;font-size:2px;color:#777}
.disc{position:absolute;border-radius:50%}
</style>
</head>
<body>

<!-- Title lockup -->
<div class="firm" style="left:31px;top:32px;font-size:6px"><span class="mark"></span><span><span class="name">TOLLAND &amp; REEVE, P.C.</span><span class="tag" style="color:#d8d8d8">Attorneys and Counselors at Law</span></span></div>
<div class="caption" style="left:43px;top:44px;font-size:3.6px;color:#d0d0d0">Stationary Concepts</div>

<!-- Business card front -->
<section class="piece card-front" style="left:33px;top:54px;width:47px;height:27px">
  <div class="firm" style="left:5px;top:3px;font-size:2.6px"><span class="mark"></span><span><span class="name">TOLLAND &amp; REEVE, P.C.</span><span class="tag">Attorneys and Counselors at Law</span></span></div>
  <div class="tiny" style="left:10px;top:9.5px;font-size:2.1px;font-weight:600">Corwin T. Tolland, Esq.</div>
  <div class="tiny" style="left:17px;top:12.4px;font-size:1.6px">Partner</div>
  <div class="tiny" style="left:4px;top:18px;font-size:1.15px">83 E. Birchfield Ln, Hicksville, NY 11947 | T. 516-555-0142 | F. 516-555-0187<br>314 Halvorsen Avenue, Suite 2200, New York, NY 10038 | T. 212-555-0163<br>ctolland@tollandlegal.example | www.tollandlegal.example</div>
</section>
<div class="caption" style="left:43px;top:83px">Front Card Option</div>

<!-- Business card backs -->
<section class="piece grey card-back" style="left:7px;top:91px;width:47px;height:26px">
  <div class="firm light" style="left:7px;top:8px;font-size:3.4px"><span class="mark"></span><span class="name">TOLLAND &amp; REEVE</span></div>
  <div class="web" style="left:13px;top:18.5px;font-size:1.5px">www.tollandlegal.example</div>
</section>
<section class="piece navy card-back" style="left:58px;top:91px;width:47px;height:26px">
  <div class="firm light" style="left:7px;top:8px;font-size:3.4px"><span class="mark"></span><span class="name">TOLLAND &amp; REEVE</span></div>
  <div class="web" style="left:13px;top:18.5px;font-size:1.5px">www.tollandlegal.example</div>
</section>
<div class="caption" style="left:17px;top:118px">Back Card Option 01</div>
<div class="caption" style="left:68px;top:118px">Back Card Option 02</div>

<!-- Letterheads -->
<section class="piece letterhead" style="left:109px;top:15px;width:79px;height:101px">
  <div class="firm" style="left:6px;top:5px;font-size:2.5px"><span class="mark"></span><span><span class="name">TOLLAND &amp; REEVE, P.C.</span><span class="tag">Attorneys and Counselors at Law</span></span></div>
  <div class="tiny" style="left:42px;top:5px;font-size:1.2px">83 E. Birchfield Ln<br>Hicksville, NY 11947<br>314 Halvorsen Avenue<br>New York, NY 10038</div>
  <div class="tiny" style="left:58px;top:5px;font-size:1.2px">T. 516-555-0142<br>F. 516-555-0187<br>T. 212-555-0163<br>www.tollandlegal.example</div>
  <div class="tiny" style="left:6px;top:22px;font-size:1.3px">Date<br><br><b>Recipient Name</b><br>Company Name<br>Street Address<br>City, State, Zip</div>
  <div class="body-lines" style="left:6px;top:40px;width:67px"><i></i><i></i><i></i><i></i><i style="width:70%"></i><i></i><i></i><i></i><i style="width:55%"></i><i></i><i></i><i style="width:80%"></i></div>
  <div role="img" aria-label="Handwritten signature" style="position:absolute;left:6px;top:82px;width:14px;height:4px;background:#d7dde3"></div>
  <div class="tiny" style="left:6px;top:87px;font-size:1.3px">Corwin T. Tolland, Esq.</div>
  <div class="tiny" style="left:22px;top:96px;font-size:1px">www.tollandlegal.example</div>
</section>
<section class="piece letterhead" style="left:192px;top:15px;width:79px;height:101px">
  <div class="firm" style="left:26px;top:5px;font-size:2.5px"><span class="mark"></span><span><span class="name">TOLLAND &amp; REEVE, P.C.</span><span class="tag">Attorneys and Counselors at Law</span></span></div>
  <div class="tiny" style="left:6px;top:13px;font-size:1.1px">CORWIN T. TOLLAND, ESQ. (Admitted in NY and NJ)<br>GERALD BERTRAM REEVE, ESQ. (Admitted in NY)</div>
  <div class="tiny" style="left:6px;top:22px;font-size:1.3px">Date<br><br><b>Recipient Name</b><br>Company Name<br>Street Address<br>City, State, Zip</div>
  <div class="body-lines" style="left:6px;top:40px;width:67px"><i></i><i></i><i></i><i></i><i style="width:70%"></i><i></i><i></i><i></i><i style="width:55%"></i><i></i><i></i><i style="width:80%"></i></div>
  <div role="img" aria-label="Handwritten signature" style="position:absolute;left:6px;top:82px;width:14px;height:4px;background:#d7dde3"></div>
  <div class="tiny" style="left:6px;top:87px;font-size:1.3px">Corwin T. Tolland, Esq.</div>
  <div class="tiny" style="left:10px;top:93px;font-size:1px">83 E. Birchfield Ln, Hicksville, NY 11947 | T. 516-555-0142 | F. 516-555-0187<br>314 Halvorsen Avenue, Suite 2200, New York, NY 10038 | T. 212-555-0163</div>
</section>
<div class="caption" style="left:139px;top:118px">Letterhead Option 01</div>
<div class="caption" style="left:222px;top:118px">Letterhead Option 02</div>

<!-- Email signature -->
<section class="piece email-signature" style="left:294px;top:40px;width:42px;height:28px">
  <div class="firm" style="left:3px;top:3px;font-size:2.4px"><span class="mark"></span><span><span class="name">TOLLAND &amp; REEVE, P.C.</span><span class="tag">Attorneys and Counselors at Law</span></span></div>
  <div class="tiny" style="left:12px;top:11px;font-size:1.6px;font-weight:600">Corwin T. Tolland, Esq.</div>
  <div class="tiny" style="left:17px;top:13.6px;font-size:1.3px">Partner</div>
  <div class="tiny" style="left:4px;top:18px;font-size:1px">83 E. Birchfield Ln, Hicksville, NY 11947 | T. 516-555-0142<br>314 Halvorsen Avenue, Suite 2200, New York, NY 10038<br>ctolland@tollandlegal.example</div>
</section>
<div class="caption" style="left:306px;top:70px">Email Signature</div>

<!-- Envelopes -->
<section class="piece envelope" style="left:276px;top:79px;width:84px;height:37px">
  <div class="firm" style="left:3px;top:4px;font-size:2.3px"><span class="mark"></span><span><span class="name">TOLLAND &amp; REEVE, P.C.</span><span class="tag">Attorneys and Counselors at Law</span></span></div>
  <div class="tiny" style="left:3px;top:10px;font-size:1px">83 E. Birchfield Ln<br>Hicksville, NY 11947<br>www.tollandlegal.example</div>
</section>
<section class="piece envelope-back" style="left:364px;top:79px;width:85px;height:37px">
  <svg width="85" height="37" viewBox="0 0 85 37" aria-hidden="true"><polygon points="0,0 85,0 42.5,18" fill="var(--navy)"/><polyline points="0,37 42.5,15 85,37" fill="none" stroke="#ddd" stroke-width=".5"/></svg>
  <div class="firm light" style="left:33px;top:4px;font-size:2.4px"><span class="mark"></span><span class="name">TOLLAND &amp; REEVE</span></div>
</section>
<div class="caption" style="left:309px;top:118px">Envelope Front</div>
<div class="caption" style="left:398px;top:118px">Envelope Back</div>

<!-- Folder -->
<section class="piece folder" style="left:466px;top:18px;width:124px;height:99px">
  <div class="navy" style="position:absolute;left:0;top:0;width:62px;height:99px"></div>
  <div class="tiny" style="left:7px;top:58px;font-size:1.1px;color:#e6eef4">83 E. Birchfield Ln<br>Hicksville, NY 11947<br>314 Halvorsen Avenue<br>New York, NY 10038<br>T. 516-555-0142</div>
  <div class="firm" style="left:74px;top:36px;font-size:2.6px"><span class="mark"></span><span><span class="name">TOLLAND &amp; REEVE, P.C.</span><span class="tag">Attorneys and Counselors at Law</span></span></div>
  <div class="navy" style="position:absolute;left:62px;top:74px;width:62px;height:25px;background:var(--navy-dark)"></div>
  <div style="position:absolute;left:80px;top:78px;width:20px;height:11px;background:var(--paper)"></div>
</section>
<div class="caption" style="left:522px;top:118px">Folder</div>

<!-- Fax sheets -->
<section class="piece fax" style="left:595px;top:15px;width:79px;height:101px">
  <div class="firm" style="left:5px;top:5px;font-size:2.4px"><span class="mark"></span><span><span class="name">TOLLAND &amp; REEVE, P.C.</span><span class="tag">Attorneys and Counselors at Law</span></span></div>
  <div class="tiny" style="left:47px;top:5px;font-size:1.1px">83 E. Birchfield Ln<br>Hicksville, NY 11947<br>T. 516-555-0142</div>
  <div class="tiny" style="left:5px;top:20px;font-size:1.3px;line-height:2.1">To<br>Fax<br>Phone<br>Re</div>
  <div class="tiny" style="left:40px;top:20px;font-size:1.3px;line-height:2.1">From<br>Pages<br>Date<br>CC</div>
  <div class="tiny" style="left:5px;top:42px;font-size:1.3px">Comments:</div>
  <div class="tiny" style="left:20px;top:93px;font-size:1px">www.tollandlegal.example</div>
</section>
<section class="piece fax" style="left:678px;top:15px;width:79px;height:101px">
  <div class="firm" style="left:26px;top:5px;font-size:2.4px"><span class="mark"></span><span><span class="name">TOLLAND &amp; REEVE, P.C.</span><span class="tag">Attorneys and Counselors at Law</span></span></div>
  <div class="tiny" style="left:5px;top:20px;font-size:1.3px;line-height:2.1">To<br>Fax<br>Phone<br>Re</div>
  <div class="tiny" style="left:40px;top:20px;font-size:1.3px;line-height:2.1">From<br>Pages<br>Date<br>CC</div>
  <div class="tiny" style="left:5px;top:42px;font-size:1.3px">Comments:</div>
  <div class="tiny" style="left:10px;top:93px;font-size:1px">83 E. Birchfield Ln, Hicksville, NY 11947 | T. 516-555-0142</div>
</section>
<div class="caption" style="left:627px;top:118px">Fax Option 01</div>
<div class="caption" style="left:710px;top:118px">Fax Option 02</div>

<!-- Compliment slip & thank you cards -->
<section class="piece compliment-slip" style="left:770px;top:27px;width:86px;height:37px">
  <div class="firm" style="left:4px;top:4px;font-size:2.4px"><span class="mark"></span><span><span class="name">TOLLAND &amp; REEVE, P.C.</span><span class="tag">Attorneys and Counselors at Law</span></span></div>
  <div class="tiny" style="left:54px;top:4px;font-size:1px">83 E. Birchfield Ln<br>Hicksville, NY 11947<br>T. 516-555-0142</div>
  <div class="script" style="left:20px;top:18px;font-size:7px">With Compliments</div>
</section>
<div class="caption" style="left:803px;top:66px">Compliment Slip</div>
<section class="piece thank-you" style="left:764px;top:72px;width:48px;height:37px">
  <div class="firm" style="left:3px;top:3px;font-size:2px"><span class="mark"></span><span class="name">TOLLAND &amp; REEVE, P.C.</span></div>
  <div class="script" style="left:8px;top:17px;font-size:7.5px">Thank you</div>
</section>
<section class="piece navy thank-you" style="left:819px;top:72px;width:47px;height:37px">
  <div class="firm light" style="left:10px;top:14px;font-size:2.3px"><span class="mark"></span><span class="name">TOLLAND &amp; REEVE</span></div>
  <div class="tiny" style="left:8px;top:26px;font-size:.9px;color:#dfe8ef">83 E. Birchfield Ln, Hicksville, NY 11947<br>T. 516-555-0142 | www.tollandlegal.example</div>
</section>
<div class="caption" style="left:776px;top:111px">Thank You Card, Front</div>
<div class="caption" style="left:831px;top:111px">Thank You Card, Back</div>

<!-- CD and CD cover -->
<div class="disc navy" style="left:864px;top:7px;width:58px;height:58px">
  <div class="firm light" style="left:15px;top:10px;font-size:2.2px"><span class="mark"></span><span class="name">TOLLAND &amp; REEVE</span></div>
  <div class="disc" style="left:20px;top:20px;width:18px;height:18px;background:var(--white)"><div class="disc" style="left:5px;top:5px;width:8px;height:8px;background:var(--bg)"></div></div>
</div>
<div class="caption" style="left:890px;top:67px">CD</div>
<section class="piece cd-cover" style="left:935px;top:12px;width:55px;height:49px">
  <div class="navy" style="position:absolute;left:0;top:0;width:55px;height:16px"></div>
  <div class="firm light" style="left:4px;top:6px;font-size:2.2px"><span class="mark"></span><span class="name">TOLLAND &amp; REEVE, P.C.</span></div>
</section>
<div class="caption" style="left:955px;top:63px">CD Cover</div>

<!-- Presentation slides -->
<section class="piece slide" style="left:1002px;top:13px;width:92px;height:70px">
  <div class="firm" style="left:18px;top:17px;font-size:3.6px"><span class="mark"></span><span><span class="name">TOLLAND &amp; REEVE, P.C.</span><span class="tag">Attorneys and Counselors at Law</span></span></div>
  <div style="position:absolute;left:0;width:92px;top:40px;text-align:center;color:var(--navy);font-size:3.4px;line-height:1.3">Welcome to Our<br><b style="font-size:4.4px">Presentation Name</b><br><span style="color:#555;font-size:3px">Description</span></div>
</section>
<section class="piece slide" style="left:1101px;top:13px;width:92px;height:70px">
  <div class="heading" style="left:5px;top:5px">Heading Here</div><div class="sub" style="left:5px;top:10px">Sub Heading</div>
  <div class="firm" style="left:77px;top:5px;font-size:3px"><span class="mark"></span></div>
  <div style="position:absolute;left:5px;top:17px;width:82px;display:flex;justify-content:space-between">
    <div role="img" aria-label="Team member photo" style="width:18px;height:17px;background:#5a5a5a"></div>
    <div role="img" aria-label="Team member photo" style="width:18px;height:17px;background:#5a5a5a"></div>
    <div role="img" aria-label="Team member photo" style="width:18px;height:17px;background:#5a5a5a"></div>
    <div role="img" aria-label="Team member photo" style="width:18px;height:17px;background:#5a5a5a"></div>
  </div>
  <div class="tiny" style="left:5px;top:37px;font-size:1.5px;color:var(--navy);word-spacing:11px">Member1 Member2 Member3 Member4</div>
  <div class="body-lines" style="left:5px;top:42px;width:82px;gap:1.3px"><i></i><i></i><i></i></div>
</section>
<section class="piece slide" style="left:1002px;top:88px;width:92px;height:70px">
  <div class="heading" style="left:5px;top:5px">Heading Here</div><div class="sub" style="left:5px;top:10px">Sub Heading</div>
  <div class="firm" style="left:77px;top:5px;font-size:3px"><span class="mark"></span></div>
  <div class="tiny" style="left:5px;top:17px;font-size:1.6px;color:var(--navy);line-height:8.5">Group1<br>Group2<br>Group3</div>
  <div class="tiny" style="left:47px;top:17px;font-size:1.6px;color:var(--navy);line-height:8.5">Group4<br>Group5<br>Group6</div>
  <div class="body-lines" style="left:5px;top:23px;width:38px;gap:1.2px"><i></i><i></i><i></i></div>
  <div class="body-lines" style="left:47px;top:23px;width:38px;gap:1.2px"><i></i><i></i><i></i></div>
</section>
<section class="piece slide" style="left:1101px;top:88px;width:92px;height:70px">
  <div class="heading" style="left:5px;top:5px">Heading Here</div><div class="sub" style="left:5px;top:10px">Sub Heading</div>
  <div class="firm" style="left:77px;top:5px;font-size:3px"><span class="mark"></span></div>
  <svg style="position:absolute;left:8px;top:18px" width="40" height="30" viewBox="0 0 40 30" aria-label="Bar chart" role="img">
    <line x1="0" y1="29.5" x2="40" y2="29.5" stroke="#999" stroke-width=".4"/>
    <rect x="2" y="4" width="4" height="25.5" fill="var(--navy)"/><rect x="8" y="7" width="4" height="22.5" fill="var(--navy)"/>
    <rect x="14" y="2" width="4" height="27.5" fill="var(--navy)"/><rect x="20" y="10" width="4" height="19.5" fill="var(--navy)"/>
    <rect x="26" y="14" width="4" height="15.5" fill="var(--navy)"/><rect x="32" y="18" width="4" height="11.5" fill="var(--navy)"/>
  </svg>
  <div class="body-lines" style="left:53px;top:18px;width:34px;gap:1.2px"><i></i><i></i><i></i><i></i><i></i><i></i></div>
</section>
<section class="piece slide" style="left:1002px;top:165px;width:92px;height:70px">
  <div class="heading" style="left:5px;top:5px">Heading Here</div><div class="sub" style="left:5px;top:10px">Sub Heading</div>
  <div class="firm" style="left:77px;top:5px;font-size:3px"><span class="mark"></span></div>
  <div class="body-lines" style="left:5px;top:18px;width:44px;gap:1.2px"><i></i><i></i><i></i><i></i><i></i><i></i><i></i><i></i><i></i><i></i></div>
  <svg style="position:absolute;left:56px;top:20px" width="24" height="24" viewBox="0 0 24 24" role="img" aria-label="Pie chart">
    <circle cx="12" cy="12" r="10" fill="var(--navy)"/>
    <path d="M12 12 L12 2 A10 10 0 0 1 21.5 9 Z" fill="#9aa9b5"/>
    <path d="M12 12 L21.5 9 A10 10 0 0 1 19 19 Z" fill="#4b6e8a"/>
  </svg>
</section>
<section class="piece navy slide" style="left:1101px;top:165px;width:92px;height:70px">
  <div style="position:absolute;left:0;width:92px;top:22px;text-align:center;font-size:11px;line-height:1;color:var(--white)">Thanks<br><span style="font-size:7px">For Coming</span></div>
  <div class="tiny" style="left:16px;top:56px;font-size:1px;color:#dfe8ef;text-align:right">83 E. Birchfield Ln, Hicksville, NY 11947 | T. 516-555-0142<br>314 Halvorsen Avenue, Suite 2200, New York, NY 10038<br>ctolland@tollandlegal.example | www.tollandlegal.example</div>
</section>

<!-- Folder inner -->
<section class="piece folder-inner" style="left:475px;top:137px;width:121px;height:75px">
  <svg width="121" height="75" viewBox="0 0 121 75" aria-hidden="true">
    <polygon points="8,47 56,47 60,75 8,75" fill="var(--navy)"/>
    <polygon points="65,47 113,47 113,75 61,75" fill="var(--navy)"/>
  </svg>
</section>
<div class="caption" style="left:528px;top:213px">Folder Inner</div>

<!-- Car magnets -->
<div class="disc" style="left:484px;top:222px;width:20px;height:20px;background:var(--paper-soft)"></div>
<div class="disc navy" style="left:511px;top:222px;width:20px;height:20px"></div>
<div class="disc" style="left:537px;top:222px;width:20px;height:20px;background:#000"></div>
<div class="disc" style="left:563px;top:222px;width:20px;height:20px;background:var(--paper-soft)"></div>
<div class="firm" style="left:488px;top:231px;font-size:1.6px"><span class="name">TOLLAND</span></div>
<div class="firm light" style="left:515px;top:231px;font-size:1.6px"><span class="name">TOLLAND</span></div>
<div class="firm light" style="left:541px;top:231px;font-size:1.6px"><span class="name">TOLLAND</span></div>
<div class="firm" style="left:567px;top:231px;font-size:1.6px"><span class="name">TOLLAND</span></div>
<div class="caption" style="left:526px;top:246px">Car Magnet</div>

<!-- CDs -->
<div class="disc navy" style="left:683px;top:130px;width:57px;height:57px"><div class="disc" style="left:19px;top:19px;width:19px;height:19px;background:var(--white)"></div></div>
<div class="disc" style="left:748px;top:130px;width:57px;height:57px;background:#000"><div class="disc" style="left:19px;top:19px;width:19px;height:19px;background:var(--white)"></div></div>
<div class="disc" style="left:683px;top:191px;width:57px;height:57px;background:var(--paper)"><div class="disc" style="left:19px;top:19px;width:19px;height:19px;background:#000"></div></div>
<div class="disc navy" style="left:748px;top:191px;width:57px;height:57px;border:2px solid var(--white)"><div class="disc" style="left:17px;top:17px;width:19px;height:19px;background:var(--white)"></div></div>
<div class="firm light" style="left:695px;top:139px;font-size:2.2px"><span class="name">TOLLAND &amp; REEVE</span></div>
<div class="firm light" style="left:760px;top:139px;font-size:2.2px"><span class="name">TOLLAND &amp; REEVE</span></div>
<div class="firm" style="left:695px;top:200px;font-size:2.2px"><span class="name">TOLLAND &amp; REEVE</span></div>
<div class="firm light" style="left:760px;top:200px;font-size:2.2px"><span class="name">TOLLAND &amp; REEVE</span></div>

<!-- CD covers -->
<section class="piece navy cd-cover" style="left:820px;top:140px;width:58px;height:42px">
  <div class="firm light" style="left:3px;top:4px;font-size:2.1px"><span class="mark"></span><span class="name">TOLLAND &amp; REEVE, P.C.</span></div>
  <div class="tiny" style="left:3px;top:36px;font-size:.9px;color:#dfe8ef">83 E. Birchfield Ln, Hicksville, NY 11947 | T. 516-555-0142</div>
</section>
<section class="piece cd-cover" style="left:820px;top:196px;width:58px;height:42px">
  <div class="firm" style="left:3px;top:4px;font-size:2.1px"><span class="mark"></span><span class="name">TOLLAND &amp; REEVE, P.C.</span></div>
  <div class="tiny" style="left:3px;top:36px;font-size:.9px">83 E. Birchfield Ln, Hicksville, NY 11947 | T. 516-555-0142</div>
</section>
<div class="caption" style="left:841px;top:184px">CD Cover</div>
<div class="caption" style="left:841px;top:240px">CD Cover</div>

</body>
</html>
```